BrickaFun Business Card

We need a business card design for our company. We sell construction-themed amusement rides for kids.

Contact Information for Business Card

Contact info on business card should include:
Dale Hurst
Co-Founder & COO
(833) 517-BRICKAF
Dale@brickafun.com
www.brickafun.com

```html
<!DOCTYPE html>
<html lang="en">
<head>
<meta charset="UTF-8">
<title>BrickaFun Business Card</title>
<link href="https://fonts.googleapis.com/css2?family=Open+Sans:wght@400;600;800&display=swap" rel="stylesheet">
<style>
  :root {
    --canvas-bg: #e6e7ea;
    --card-bg: #ffffff;
    --brand-orange: #f26a2e;
    --brand-purple: #9b2bb3;
    --text-dark: #2b2b2b;
    --photo-top: #f3cf3a;
    --photo-bottom: #c9a21f;
    --photo-dark: #3a3a3a;
  }
  * { box-sizing: border-box; margin: 0; padding: 0; }
  html, body { width: 1200px; height: 811px; overflow: hidden; }
  body {
    background: var(--canvas-bg);
    font-family: "Open Sans", Arial, sans-serif;
    position: relative;
  }
  .card {
    position: absolute;
    top: 251px;
    width: 540px;
    height: 309px;
    background: var(--card-bg);
    box-shadow: 0 4px 14px rgba(0,0,0,0.12);
  }
  .card--back { left: 40px; }
  .card--front { left: 620px; }

  .brand {
    display: flex;
    align-items: center;
    gap: 10px;
    font-weight: 800;
    color: var(--brand-orange);
    letter-spacing: -0.5px;
  }
  .brand__dot {
    border-radius: 50%;
    background: var(--brand-purple);
    flex: none;
  }
  .card--back .brand {
    position: absolute;
    left: 50%; top: 50%;
    transform: translate(-50%, -50%);
    font-size: 54px;
  }
  .card--back .brand__dot { width: 30px; height: 30px; }

  .card--front .brand {
    position: absolute;
    left: 34px; top: 58px;
    font-size: 34px;
  }
  .card--front .brand__dot { width: 20px; height: 20px; }

  .product-photo {
    position: absolute;
    left: 300px; top: 30px;
    width: 210px; height: 160px;
    background: linear-gradient(160deg, var(--photo-top) 0%, var(--photo-bottom) 70%, var(--photo-dark) 100%);
    border-radius: 6px;
  }

  .contact-person {
    position: absolute;
    left: 46px; top: 160px;
  }
  .contact-person__name {
    font-size: 19px;
    font-weight: 600;
    color: var(--brand-purple);
    line-height: 1.2;
  }
  .contact-person__title {
    font-size: 12px;
    color: var(--text-dark);
    margin-top: 2px;
  }
  .contact-list {
    position: absolute;
    left: 46px; top: 228px;
    list-style: none;
  }
  .contact-list__item {
    display: flex;
    align-items: center;
    gap: 10px;
    font-size: 12px;
    color: var(--text-dark);
    height: 20px;
  }
  .contact-list__icon { width: 12px; height: 12px; flex: none; }
</style>
</head>
<body>
  <section class="card card--back" aria-label="Card back">
    <div class="brand"><span class="brand__dot"></span>BrickaFun</div>
  </section>

  <section class="card card--front" aria-label="Card front">
    <div class="brand"><span class="brand__dot"></span>BrickaFun</div>

    <div class="product-photo" role="img" aria-label="Photo of a yellow kids' ride-on mini excavator"></div>

    <div class="contact-person">
      <p class="contact-person__name">Dale Hurst</p>
      <p class="contact-person__title">Co-Founder &amp; COO</p>
    </div>

    <ul class="contact-list">
      <li class="contact-list__item">
        <svg class="contact-list__icon" viewBox="0 0 12 12" aria-hidden="true">
          <rect x="3" y="0.5" width="6" height="11" rx="1.2" fill="none" stroke="var(--brand-orange)" stroke-width="1.2"/>
          <circle cx="6" cy="9.5" r="0.7" fill="var(--brand-orange)"/>
        </svg>
        (833) 517-BRICKAF
      </li>
      <li class="contact-list__item">
        <svg class="contact-list__icon" viewBox="0 0 12 12" aria-hidden="true">
          <rect x="0.5" y="2" width="11" height="8" rx="1" fill="var(--brand-orange)"/>
          <path d="M1 2.6 L6 6.6 L11 2.6" fill="none" stroke="#fff" stroke-width="1"/>
        </svg>
        Dale@brickafun.com
      </li>
      <li class="contact-list__item">
        <svg class="contact-list__icon" viewBox="0 0 12 12" aria-hidden="true">
          <circle cx="6" cy="6" r="5.5" fill="var(--brand-orange)"/>
          <ellipse cx="6" cy="6" rx="2.2" ry="5" fill="none" stroke="#fff" stroke-width="0.8"/>
          <line x1="1" y1="6" x2="11" y2="6" stroke="#fff" stroke-width="0.8"/>
        </svg>
        www.brickafun.com
      </li>
    </ul>
  </section>
</body>
</html>
```